Business Card Design Project

I have just chosen a logo and would now like this designed onto a business card for my hair salon. I would like it to be classy not to busy and have a wow factor when people look at them
Has to Include on card:
Logo Design
And business details below
Kaycee-rae Whitlow (owner)
0481 726 304
Lmv@brindal.com.au
57 Corella Street Kinross Vale
Logo is now attached please provide designs
Hair

```html
<!DOCTYPE html>
<html lang="en">
<head>
<meta charset="utf-8">
<title>Lumen Hair Studio – Business Card</title>
<link rel="stylesheet" href="https://fonts.googleapis.com/css2?family=EB+Garamond:wght@400;500&display=swap">
<style>
  :root {
    --backdrop: #d9d9d9;
    --card-dark: #1c1c1e;
    --card-dark-pattern: #2a2a2d;
    --card-light: #f7f7f5;
    --ink: #1e1e1e;
    --magenta: #c8177a;
    --violet: #9a7cc0;
    --teal: #5cc3c6;
  }
  * { box-sizing: border-box; margin: 0; padding: 0; }
  html, body { width: 1200px; height: 900px; overflow: hidden; }
  body {
    background: var(--backdrop);
    font-family: "EB Garamond", Georgia, serif;
    color: var(--ink);
    position: relative;
  }
  .card {
    position: absolute;
    top: 285px;
    width: 540px;
    height: 330px;
    overflow: hidden;
    box-shadow: 0 2px 6px rgba(0,0,0,0.18);
  }
  /* Back of card */
  .card-back { left: 45px; background: var(--card-dark); }
  .card-back .damask-field {
    position: absolute; inset: 0;
    background: radial-gradient(circle at 50% 50%, var(--card-dark-pattern), var(--card-dark) 75%);
  }
  .brand-name {
    position: absolute; inset: 0;
    display: flex; flex-direction: column; align-items: center; justify-content: center;
    color: var(--magenta);
    font-weight: 500;
    text-align: center;
    line-height: 1;
  }
  .brand-name .brand-line-1 { font-size: 66px; letter-spacing: 1px; text-transform: uppercase; }
  .brand-name .brand-line-2 { font-size: 50px; margin-top: 4px; }

  /* Front of card */
  .card-front { left: 615px; background: var(--card-light); }
  .damask-column {
    position: absolute; top: 0; right: 0; width: 130px; height: 100%;
    background: linear-gradient(180deg, var(--magenta) 0%, var(--violet) 50%, var(--teal) 78%, var(--teal) 100%);
    opacity: 0.85;
  }
  .contact-block { position: absolute; left: 50px; top: 96px; }
  .person-name {
    font-size: 26px; font-weight: 400; text-transform: uppercase; letter-spacing: 0.5px;
  }
  .person-role { font-size: 21px; color: var(--teal); margin-top: -4px; }
  .details { list-style: none; margin-top: 24px; }
  .details li {
    display: flex; align-items: center; gap: 8px;
    font-size: 19px; line-height: 23px;
  }
  .details svg { width: 13px; height: 13px; flex: none; fill: var(--teal); }
</style>
</head>
<body>
  <section class="card card-back">
    <div class="damask-field" role="img" aria-label="Dark tone-on-tone damask pattern covering the card"></div>
    <div class="brand-name">
      <span class="brand-line-1">Lumen</span>
      <span class="brand-line-2">Hair Studio</span>
    </div>
  </section>

  <section class="card card-front">
    <div class="contact-block">
      <h1 class="person-name">Kaycee-rae Whitlow</h1>
      <p class="person-role">owner</p>
      <ul class="details">
        <li>
          <svg viewBox="0 0 16 16" aria-hidden="true"><circle cx="8" cy="8" r="8"/><path d="M5.2 4h1.6l.7 2-1 .8a6 6 0 0 0 2.7 2.7l.8-1 2 .7v1.6c0 .5-.4.9-.9.9A7.2 7.2 0 0 1 4.3 4.9c0-.5.4-.9.9-.9z" fill="#fff"/></svg>
          0481 726 304
        </li>
        <li>
          <svg viewBox="0 0 16 16" aria-hidden="true"><rect x="0" y="3" width="16" height="10" rx="1"/><path d="M1 4l7 5 7-5" stroke="#fff" stroke-width="1.2" fill="none"/></svg>
          Lmv@brindal.com.au
        </li>
        <li>
          <svg viewBox="0 0 16 16" aria-hidden="true"><path d="M8 0a5.5 5.5 0 0 0-5.5 5.5C2.5 9.7 8 16 8 16s5.5-6.3 5.5-10.5A5.5 5.5 0 0 0 8 0zm0 7.7a2.2 2.2 0 1 1 0-4.4 2.2 2.2 0 0 1 0 4.4z"/></svg>
          57 Corella Street Kinross Vale
        </li>
      </ul>
    </div>
    <div class="damask-column" role="img" aria-label="Column of damask ornaments fading from magenta through violet to teal"></div>
  </section>
</body>
</html>
```